Journal to help kids Grades 1-5 be more creative thinkers

This is a journal for kids grades 1 - 5 where they can write, color, draw and be creative. It is designed to accompany our children's book and after-school program called Marble Tinker Guild. We want children to use their imagination and sense of wonder as they color, create new ideas, write stories and learn all about the creative problems solving method. We want them to learn about how to use their feelings and help others in their community. We have based this on our PLANET method, which helps teachers teach their curriculum by engaging kids in relevant and meaningful ways and helping children of all ages learn how to think for themselves. We are a non-profit organization, so all the sales go to a scholarship fund that helps teachers pay for coaching and professional development. This journal may be used in after school programs, at home, or in classrooms. We wanted the inside to be black and white so kids feel free to make it their own but the cover should be bright and inviting. This is written and designed by Lorna Pavesky and Delia Ashworthy on behalf of Bluefinch 4 PLANET.

Target Market(s)

Parents, schools, after school programs

Industry/Entity Type

Education

Font styles to use
Other font styles liked:
• Fun for kids

Requirements
Must have
• Bright fun colors, our logo, easy to read font for kids
Nice to have
• Our 6 characters - but we do have them throughout book -

```html
<!DOCTYPE html>
<html lang="en">
<head>
<meta charset="UTF-8">
<title>Marble Tinker Journal — Cover</title>
<link href="https://fonts.googleapis.com/css2?family=Fredoka:wght@500;600&family=Quicksand:wght@500&display=swap" rel="stylesheet">
<style>
  :root {
    --page-bg: #ffffff;
    --cover-blue: #5f7dfc;
    --cover-violet: #9f7fe6;
    --cover-pink: #fb63c8;
    --title-white: #ffffff;
    --tag-green: #c9f0b4;
    --tag-yellow: #f7ef8a;
    --tag-peach: #fcd9b0;
    --tag-aqua: #a9ecf0;
    --tag-cream: #fbe6a6;
    --logo-ink: #ffd54a;
    --art-a: rgba(243, 201, 166, 0.55);
    --art-b: rgba(194, 212, 255, 0.35);
  }
  * { margin: 0; padding: 0; box-sizing: border-box; }
  html, body {
    width: 1200px; height: 920px; overflow: hidden;
    background: var(--page-bg);
  }
  .cover {
    position: absolute; left: 330px; top: 30px;
    width: 540px; height: 860px;
    background: linear-gradient(90deg, var(--cover-blue) 0%, var(--cover-violet) 50%, var(--cover-pink) 100%);
    font-family: "Fredoka", sans-serif;
    color: var(--title-white);
  }
  .character {
    position: absolute; width: 86px; height: 130px;
    border-radius: 30px;
    background: linear-gradient(180deg, var(--art-a), var(--art-b));
  }
  .character--musician  { left: 14px;  top: 50px; height: 150px; }
  .character--scientist { left: 14px;  top: 255px; }
  .character--chef      { left: 14px;  top: 460px; height: 150px; }
  .character--painter   { right: 16px; top: 40px; height: 160px; }
  .character--business  { right: 16px; top: 290px; height: 150px; }
  .character--explorer  { right: 16px; top: 500px; width: 130px; height: 130px; }
  .title {
    position: absolute; left: 0; right: 0; top: 138px;
    text-align: center; font-weight: 600;
    font-size: 54px; line-height: 70px; letter-spacing: 1px;
    text-shadow: 0 0 14px rgba(120, 60, 200, 0.6);
  }
  .tagline {
    position: absolute; left: 0; right: 0; top: 382px;
    text-align: center; font-weight: 600;
    font-size: 29px; line-height: 33px;
  }
  .tagline span { display: block; }
  .tagline .w1 { color: var(--tag-green); }
  .tagline .w2 { color: var(--tag-yellow); }
  .tagline .w3 { color: var(--tag-peach); }
  .tagline .w4 { color: var(--tag-aqua); }
  .tagline .w5 { color: var(--tag-cream); }
  .emblem-art {
    position: absolute; left: 195px; top: 570px;
    width: 150px; height: 90px; border-radius: 12px;
    background: linear-gradient(180deg, rgba(238, 240, 255, 0.75), rgba(183, 185, 240, 0.55));
  }
  .brand {
    position: absolute; left: 0; right: 0; top: 680px;
    display: flex; justify-content: center; align-items: center; gap: 8px;
    font-weight: 600; font-size: 25px; color: var(--logo-ink);
  }
  .brand svg { flex: none; }
  .authors {
    position: absolute; left: 0; right: 0; top: 770px;
    text-align: center; font-family: "Quicksand", sans-serif; font-weight: 500;
    font-size: 23px; line-height: 36px; letter-spacing: 3px;
  }
</style>
</head>
<body>
  <main class="cover">
    <div class="character character--musician" role="img" aria-label="Illustrated child playing guitar at a microphone"></div>
    <div class="character character--scientist" role="img" aria-label="Illustrated child scientist in lab coat with flask"></div>
    <div class="character character--chef" role="img" aria-label="Illustrated child chef carrying a dish"></div>
    <div class="character character--painter" role="img" aria-label="Illustrated child painter with palette and brush"></div>
    <div class="character character--business" role="img" aria-label="Illustrated child with briefcase pointing upward"></div>
    <div class="character character--explorer" role="img" aria-label="Illustrated child explorer with magnifier beside a tree stump"></div>

    <h1 class="title">MARBLE<br>TINKER<br>JOURNAL</h1>

    <p class="tagline">
      <span class="w1">BE</span><span class="w2">WHO</span><span class="w3">YOU</span><span class="w4">WANT</span><span class="w5">TO BE</span>
    </p>

    <div class="emblem-art" role="img" aria-label="Illustrated open book with magnifying glass"></div>
    <div class="brand">
      <svg width="14" height="14" viewBox="0 0 14 14" aria-hidden="true"><circle cx="7" cy="7" r="7" fill="#ffd54a"/></svg>
      <span>Marble Tinker Guild</span>
    </div>

    <p class="authors">BY LORNA PAVESKY AND<br>DELIA ASHWORTHY</p>
  </main>
</body>
</html>
```